Evergrove Yard Service and Beyond LLC

• Mowing
• Weed eating
•Edging
• hedge trimming
• landscaping
•mulching
•yard clean up
• pressure washing

Target Market(s)

Everyone

Contact Information for Business Card

Licensed and insured

Font styles to use
Serif

Colors
59FF00
82FF00
B8FF75
E3FFCB
F4FFEA
F0912C
F2A743
F7CA91
FBE8D2
FDF5EE
EE7325
F08F49
F5BC92
FAE3D3
FDF4ED
EB3D1F
EC4F4E
F09395
F8D3D4
FCEDEE
E54698
E96AAD
F1A4CE
F9D9EA
FCEFF6

```html
<!DOCTYPE html>
<html lang="en">
<head>
<meta charset="utf-8">
<title>Evergrove Yard Service and Beyond LLC — Business Card</title>
<link href="https://fonts.googleapis.com/css2?family=Cinzel:wght@700&family=Poppins:wght@300;400&family=Roboto:wght@400;700&display=swap" rel="stylesheet">
<style>
  :root {
    --bg: #2a2a2a;
    --green-light: #41b045;
    --green-deep: #0f9c52;
    --green-olive: #6e9a2c;
    --green-brand: #129a4a;
    --green-leaf: #8db83a;
    --band: #1c1c1e;
    --band-text: #d9d9d9;
    --ink: #1a1a1a;
    --paper: #ececea;
  }
  * { margin: 0; padding: 0; box-sizing: border-box; }
  html, body { width: 1200px; height: 1138px; overflow: hidden; }
  body { background: var(--bg); position: relative; font-family: "Roboto", sans-serif; }

  .card {
    position: absolute;
    width: 620px;
    height: 375px;
    border-radius: 16px;
    overflow: hidden;
    box-shadow: 0 4px 10px rgba(0,0,0,.45);
  }

  /* Front */
  .card--front {
    left: 274px; top: 186px;
    background: linear-gradient(200deg, var(--green-deep) 0%, var(--green-light) 45%, var(--green-light) 65%, var(--green-olive) 100%);
  }
  .brand {
    position: absolute; left: 0; right: 0;
    text-align: center;
    font-family: "Cinzel", serif; font-weight: 700;
    color: var(--ink);
  }
  .brand__main { display: block; font-size: 54px; line-height: 1; letter-spacing: 2px; }
  .brand__sub { display: block; font-size: 15px; letter-spacing: 6px; margin-top: 8px; }
  .card--front .brand { top: 88px; }

  .services {
    position: absolute; left: 0; right: 0; top: 229px; height: 71px;
    background: var(--band);
    display: flex; flex-direction: column; justify-content: center; align-items: center;
    font-family: "Poppins", sans-serif; font-weight: 300;
    font-size: 16.5px; line-height: 24px; color: var(--band-text);
    white-space: nowrap;
  }
  .services .sep { margin: 0 9px; }
  .website {
    position: absolute; left: 0; right: 0; top: 333px;
    text-align: center;
    font-family: "Poppins", sans-serif; font-weight: 400;
    font-size: 14px; color: var(--ink);
  }

  /* Back */
  .card--back {
    left: 276px; top: 608px;
    background: var(--paper);
  }
  .card--back .brand {
    left: 28px; right: auto; top: 40px; text-align: left;
    color: var(--green-brand);
  }
  .card--back .brand__main { font-size: 32px; }
  .card--back .brand__sub { font-size: 10px; letter-spacing: 4px; margin-top: 6px; }

  .decor {
    position: absolute; right: -70px; bottom: -90px;
    width: 330px; height: 330px; border-radius: 50%;
    background: radial-gradient(circle at 50% 40%, var(--green-leaf) 0%, #7fae36 55%, var(--green-brand) 100%);
  }

  .person { position: absolute; left: 28px; top: 124px; }
  .person__name { font-size: 26px; font-weight: 700; color: var(--green-brand); line-height: 1.1; }
  .person__title { font-size: 16px; color: var(--ink); margin-top: 4px; }

  .address {
    position: absolute; left: 28px; top: 210px;
    font-size: 16px; line-height: 25px; color: var(--ink); font-style: normal;
  }
  .contacts { position: absolute; left: 28px; top: 280px; list-style: none; }
  .contacts li { display: flex; align-items: center; gap: 13px; font-size: 16px; line-height: 25px; color: var(--ink); }
  .contacts svg { width: 15px; height: 15px; fill: var(--green-brand); flex: none; }
</style>
</head>
<body>

<section class="card card--front" aria-label="Business card front">
  <h1 class="brand">
    <span class="brand__main">EVERGROVE</span>
    <span class="brand__sub">YARD SERVICE &amp; BEYOND LLC</span>
  </h1>
  <div class="services">
    <p>MOWING<span class="sep">|</span>WEED EATING<span class="sep">|</span>EDGING<span class="sep">|</span>HEDGE TRIMMING</p>
    <p>LANDSCAPING<span class="sep">|</span>MULCHING<span class="sep">|</span>YARD CLEAN UP<span class="sep">|</span>PRESSURE WASHING</p>
  </div>
  <p class="website">www.evergroveyardservice.com</p>
</section>

<section class="card card--back" aria-label="Business card back">
  <div class="decor" role="img" aria-label="Large green brand decoration"></div>
  <h2 class="brand">
    <span class="brand__main">EVERGROVE</span>
    <span class="brand__sub">YARD SERVICE &amp; BEYOND LLC</span>
  </h2>
  <div class="person">
    <p class="person__name">Marcus Hale</p>
    <p class="person__title">Managing Director</p>
  </div>
  <address class="address">48 Linden Row, Fairmont,<br>Oakdale, US 204816</address>
  <ul class="contacts">
    <li>
      <svg viewBox="0 0 16 16" aria-hidden="true"><path d="M3 2c-1.2.5-2 1.5-1.7 3C2 9 7 14 11 14.7c1.5.3 2.5-.5 3-1.7l-2.6-2.1-1.6 1.2C8 11.2 4.8 8 3.9 6.2l1.2-1.6z"/></svg>
      555-014-2287
    </li>
    <li>
      <svg viewBox="0 0 16 16" aria-hidden="true"><path d="M1 3h14v10H1z M2.2 4 8 8.6 13.8 4z" fill-rule="evenodd"/></svg>
      marcus@evergroveyard.com
    </li>
    <li>
      <svg viewBox="0 0 16 16" aria-hidden="true"><path d="M8 1a7 7 0 1 0 0 14A7 7 0 0 0 8 1zm0 1.4c.8.8 1.4 2.2 1.6 3.8H6.4C6.6 4.6 7.2 3.2 8 2.4zM2.5 7.2h2.7c0 .6 0 1.1.1 1.6H2.5a5.6 5.6 0 0 1 0-1.6zm3.9 0h3.2c0 .6 0 1.1-.1 1.6H6.5c-.1-.5-.1-1-.1-1.6zm4.4 0h2.7a5.6 5.6 0 0 1 0 1.6h-2.8c.1-.5.1-1 .1-1.6zM6.5 9.8h3c-.2 1.6-.8 3-1.5 3.8-.7-.8-1.3-2.200-1.5-3.800z"/></svg>
      www.evergroveyard.com
    </li>
  </ul>
</section>

</body>
</html>
```